依頼詳細
依頼内容は以下の通りです。
・セミナーDMデザイン
・チラシで使用したイラストデータの提供(ホームページやパワーポイントに貼り付け)
・定期的なメンテナンス(2か月に1回程度、日時等の修正依頼予定)
⇒修正依頼する場合、時間的余裕を持って、別途プロジェクト登録します。

参考までに、これまで使用していたデザインと変更依頼内容を添付します。

現行デザインに固執しておりませんので、新たなデザインをお願いしたく思っております。

ご不明点等ございましたら、お問い合わせ下さい。

```html
<!DOCTYPE html>
<html lang="ja">
<head>
<meta charset="UTF-8">
<title>コロナ融資借換&資金調達セミナー</title>
<link href="https://fonts.googleapis.com/css2?family=Noto+Sans+JP:wght@500;700;900&family=Noto+Serif+JP:wght@700&display=swap" rel="stylesheet">
<style>
:root{
  --navy:#123a8c;
  --blue:#1a5fc8;
  --red:#d9121b;
  --orange:#f39800;
  --yellow:#ffe14a;
  --ink:#1a1a1a;
  --paper:#ffffff;
  --grey:#eef0f3;
  --line:#f3a64a;
}
*{box-sizing:border-box;margin:0;padding:0}
html,body{width:848px;height:1200px;overflow:hidden;background:var(--paper)}
body{font-family:"Noto Sans JP",sans-serif;color:var(--ink)}
.flyer{position:relative;width:848px;height:1200px;background:linear-gradient(180deg,#fff 0%,var(--grey) 100%);overflow:hidden}
.abs{position:absolute}

.tagline{left:40px;top:14px;font-weight:900;font-size:48px;color:var(--navy);letter-spacing:1px}
.tagline .accent{color:var(--red);font-size:60px}
.tagline .underline{border-bottom:4px solid var(--red)}
.badge-new{left:690px;top:16px;width:130px;height:104px;background:var(--red);color:#fff;font-weight:900;font-size:36px;line-height:48px;text-align:center;border-radius:8px;padding-top:4px}

.title{left:40px;font-weight:900;color:var(--blue);line-height:1;white-space:nowrap;-webkit-text-stroke:2px #fff;paint-order:stroke fill;text-shadow:3px 3px 0 rgba(0,0,0,.15)}
.title-1{top:108px;font-size:92px}
.title-1 .amp{color:var(--orange);font-size:110px;margin-left:6px}
.title-2{top:214px;font-size:90px;letter-spacing:-2px}

.scene-worry{left:40px;top:320px;width:320px;height:235px;border-radius:14px;background:radial-gradient(circle at 50% 60%,#c9d3e2,#eef1f6 70%)}
.worry{position:absolute;width:76px;height:76px;border-radius:50%;background:#fff;border:3px solid #8a96a8;font-weight:700;font-size:17px;display:flex;align-items:center;justify-content:center;text-align:center;line-height:1.1}
.sos{position:absolute;left:130px;top:150px;color:var(--red);font-weight:900;font-size:26px}

.arrow{left:0;top:280px;width:848px;height:520px}
.silhouette{left:725px;top:440px;width:105px;height:240px;border-radius:50px 50px 8px 8px;background:linear-gradient(180deg,#3a3f4a,#1c1f26)}

.merits{left:430px;top:410px}
.merit{display:flex;align-items:center;height:60px;margin-bottom:8px}
.merit-icon{width:48px;height:48px;flex:none;border-radius:50%;background:var(--red);margin-right:12px;display:flex;align-items:center;justify-content:center}
.merit-text{font-weight:900;color:var(--navy);-webkit-text-stroke:6px #fff;paint-order:stroke fill;white-space:nowrap}
.merit-1{font-size:48px}
.merit-2{font-size:42px}
.merit-3{font-size:42px}

.portrait{left:0;top:565px;width:425px;height:553px;background:linear-gradient(180deg,#dfe6ef 0%,#9aa7bb 100%)}
.catch{left:440px;top:625px;writing-mode:vertical-rl;font-weight:900;font-size:28px;color:var(--navy);background:#fff;padding:8px 6px;border:3px solid var(--navy);border-radius:6px;line-height:1.25}
.name-block{left:24px;top:890px;writing-mode:vertical-rl;display:flex;gap:6px;align-items:flex-start}
.name-role{font-size:13px;font-weight:700;color:var(--ink);background:rgba(255,255,255,.85);padding:4px 2px;line-height:1.4}
.name{font-family:"Noto Serif JP",serif;font-size:40px;font-weight:700;color:var(--ink);background:rgba(255,255,255,.85);padding:6px 2px;letter-spacing:4px}

.apply{left:518px;top:730px;width:318px}
.apply-head{background:var(--orange);color:#fff;font-weight:900;font-size:19px;text-align:center;border-radius:16px;padding:2px 0;margin-bottom:4px}
.row{display:flex;align-items:center;border-bottom:1px dotted var(--line);min-height:38px;padding:2px 0;font-size:12px}
.row .label{width:70px;flex:none;background:var(--navy);color:#fff;font-weight:700;text-align:center;padding:4px 0;margin-right:7px;font-size:12px}
.row .value{font-weight:700;line-height:1.25}
.big{font-size:18px;font-weight:900}
.small{font-size:10px;font-weight:500}
.note-red{color:#fff;background:var(--red);font-size:10px;padding:1px 4px;margin-left:4px;white-space:nowrap}
.phone{color:var(--red)}

.bonus{left:518px;top:1012px;width:318px;height:96px;display:flex;align-items:center;gap:7px}
.bonus-badge{width:62px;height:62px;flex:none;border-radius:50%;background:var(--red);color:#fff;font-weight:900;font-size:13px;display:flex;align-items:center;justify-content:center;text-align:center;line-height:1.15}
.bonus-book{width:48px;height:66px;flex:none;background:linear-gradient(160deg,#fff7c9,#f2c94c);border:1px solid #c9a43b}
.bonus-text{flex:1;font-weight:700;font-size:12px;line-height:1.4;color:var(--ink)}
.bonus-text strong{color:var(--red)}

.footer{left:0;top:1118px;width:848px;height:82px;background:var(--navy);display:flex;align-items:center;justify-content:center}
.footer p{color:#fff;font-weight:700;font-size:23px;line-height:1.4;text-align:center}
.footer .hl{color:var(--yellow)}
</style>
</head>
<body>
<div class="flyer">

  <svg class="abs arrow" viewBox="0 0 848 520" aria-hidden="true">
    <defs>
      <linearGradient id="arrowFill" x1="0" y1="1" x2="1" y2="0">
        <stop offset="0" stop-color="#ffe9a8"/>
        <stop offset=".5" stop-color="#f7b63a"/>
        <stop offset="1" stop-color="#f08a00"/>
      </linearGradient>
    </defs>
    <path d="M0 470 C 250 450, 480 340, 640 160 L 600 130 L 760 60 L 730 230 L 690 200 C 530 390, 290 500, 0 520 Z" fill="url(#arrowFill)" opacity=".9"/>
  </svg>

  <div class="abs tagline"><span class="accent">脱</span><span class="underline">コロナ禍</span>を実現する!</div>
  <div class="abs badge-new">最新<br>実務</div>

  <div class="abs title title-1">コロナ融資借換<span class="amp">&amp;</span></div>
  <div class="abs title title-2">資金調達セミナー</div>

  <div class="abs scene-worry" role="img" aria-label="頭を抱える経営者と経営課題の吹き出しのイラスト">
    <div class="worry" style="left:20px;top:10px">人手<br>不足</div>
    <div class="worry" style="left:120px;top:0">円安</div>
    <div class="worry" style="left:220px;top:10px">返済<br>開始</div>
    <div class="worry" style="left:10px;top:110px">物価高</div>
    <div class="worry" style="left:230px;top:110px">過剰<br>債務</div>
    <div class="sos">SOS!</div>
  </div>

  <div class="abs silhouette" role="img" aria-label="矢印の先に立つビジネスマンのシルエット"></div>

  <div class="abs merits">
    <div class="merit">
      <span class="merit-icon"><svg width="28" height="28" viewBox="0 0 30 30"><path d="M4 24 L12 15 L17 19 L26 7" stroke="#fff" stroke-width="4" fill="none"/><path d="M20 6 H27 V13" stroke="#fff" stroke-width="4" fill="none"/></svg></span>
      <span class="merit-text merit-1">業績回復!!!</span>
    </div>
    <div class="merit">
      <span class="merit-icon"><svg width="28" height="28" viewBox="0 0 30 30"><circle cx="15" cy="15" r="10" stroke="#fff" stroke-width="3.5" fill="none"/><path d="M10 10 L15 16 L20 10 M10 17 H20 M15 16 V23" stroke="#fff" stroke-width="2.5" fill="none"/></svg></span>
      <span class="merit-text merit-2">資金繰り改善!!</span>
    </div>
    <div class="merit">
      <span class="merit-icon"><svg width="28" height="28" viewBox="0 0 30 30"><rect x="7" y="5" width="16" height="20" stroke="#fff" stroke-width="3" fill="none"/><path d="M11 11 H19 M11 16 H19 M11 21 H16" stroke="#fff" stroke-width="2.5"/></svg></span>
      <span class="merit-text merit-3">経営計画の策定!</span>
    </div>
  </div>

  <div class="abs portrait" role="img" aria-label="講師のスーツ姿の人物写真"></div>
  <div class="abs catch">今、やるべき事が<br>分かります!</div>
  <div class="abs name-block">
    <span class="name-role">セミナー講師<br>田中経営事務所 代表</span>
    <span class="name">田中 誠一</span>
  </div>

  <section class="abs apply">
    <div class="apply-head">● セミナー応募要項 ●</div>
    <div class="row"><span class="label">日 時</span><span class="value"><span class="big">4月19日</span>(水)〜<span class="big">5月11日</span>(木)<br><span class="small">毎日開催 14:00〜16:00</span></span></div>
    <div class="row"><span class="label">会 場</span><span class="value"><span class="big">中央ビジネスセンター</span><br><span class="small">市内中央区本町1-2-3 第3会議室</span></span></div>
    <div class="row"><span class="label">受講料</span><span class="value">税込 <span class="big">10,000円</span><span class="note-red">早期お申込特典あり</span></span></div>
    <div class="row"><span class="label">主 催</span><span class="value"><span class="small">経済産業省認定支援機関</span><br>田中経営事務所</span></div>
    <div class="row"><span class="label">お申込期限</span><span class="value"><span class="big">4月7日</span>(金) <span class="small">必着 FAXにて受付</span></span></div>
    <div class="row"><span class="label">お問合せ先</span><span class="value"><span class="small">田中経営事務所</span><br><span class="big phone">TEL.075-000-1234</span></span></div>
  </section>

  <div class="abs bonus">
    <div class="bonus-badge">早期<br>お申込<br>特典</div>
    <div class="bonus-book" role="img" aria-label="特典冊子の表紙"></div>
    <p class="bonus-text"><strong>3月31日(金)</strong>までのお申込で<br>【銀行格付け丸わかりガイド】を<br>もれなく<strong>プレゼント!!</strong></p>
  </div>

  <div class="abs footer">
    <p>お申込は<span class="hl">裏面の必要事項</span>をご記入の上、<br><span class="hl">FAX</span>にてお送りください。</p>
  </div>

</div>
</body>
</html>
```